Roofing web site brel roofing

Look at some of our competitors web page we like something similar with NYC roofing
https://www.dovantileworks.example/
Maybe a skyline picture of nyc at the home page with a picture of flat roofing installation

Target Market(s)

Commercial and residential flat roofs

Industry/Entity Type

Flat Roofing industry

Coding

Coded - Design and coding required

Number of Pages Required

2 page

Font styles to use
Decorative
Script

Colors

Designer to choose colors to be used in the design.

Requirements
Must have
• At BREL Roofing, we are a trusted and reputable roofing company specializing in new construction flat roof installation and repair. With years of experience in the industry, we take pride in providing exceptional roofing solutions to our valued clients. Our team of highly skilled and dedicated roofing professionals understands the unique challenges and requirements of new construction projects. We work closely with builders, contractors, and architects to design and install flat roofs that meet the specific needs of each project. From commercial buildings to residential complexes, we have the expertise to deliver reliable and durable roofing solutions. When it comes to flat roof repairs, we are your go-to experts. Our experienced technicians conduct thorough inspections to identify the root cause of any issues your roof may be experiencing. We utilize the latest industry techniques and high-quality materials to efficiently repair your flat roof, ensuring its integrity and longevity. At BREL Roofing, we prioritize customer satisfaction above all else. We believe in building strong relationships with our clients by providing exceptional craftsmanship and outstanding customer service. Our team is dedicated to delivering projects on time, within budget, and to the highest standards of quality. We understand that a well-maintained roof is essential for protecting your property and ensuring the safety of its occupants. That's why we use only the best materials and employ skilled professionals who are trained in the latest roofing practices. Our commitment to excellence is evident in every project we undertake. As a fully licensed and insured roofing company, we prioritize safety and adhere to industry regulations and best practices. We take every precaution to create a safe working environment for our team and minimize any disruptions to your daily routine. When you choose BREL Roofing, you can trust that you are working with a reliable and reputable company that will deliver exceptional results. We are committed to exceeding your expectations and providing you with a roof that is built to last. Contact us today for all your new construction flat roof installation and repair needs.
Nice to have
• NYC skyline background with commercial roofing pictures of torching roofing

```html
<!DOCTYPE html>
<html lang="en">
<head>
<meta charset="utf-8">
<title>BREL Roofing</title>
<link href="https://fonts.googleapis.com/css2?family=Inter:wght@400;500;600;700;800&display=swap" rel="stylesheet">
<style>
:root{
  --navy:#0b1a4f;
  --orange:#f36b1c;
  --ink:#1b1b1b;
  --muted:#4a4a4a;
  --line:#dde2ea;
  --pale:#eef1f6;
  --white:#ffffff;
}
*{box-sizing:border-box;margin:0;padding:0}
html,body{width:1200px;height:3810px;overflow:hidden}
body{position:relative;background:var(--white);font-family:'Inter',sans-serif;color:var(--ink)}
.abs{position:absolute}
.photo{position:absolute;overflow:hidden}
.brand-box{position:absolute;border:1.5px solid var(--navy);display:flex;align-items:center;justify-content:center;text-align:center;font-size:20px;font-weight:400;color:var(--navy);line-height:1.25}
.nav{position:absolute;top:36px;left:535px;display:flex;gap:28px;font-size:13.5px}
.nav a{color:var(--ink);text-decoration:none;padding-bottom:8px}
.nav a.active{border-bottom:2px solid var(--orange)}
.phone-btn{position:absolute;display:flex;align-items:center;gap:10px;border-radius:4px;font-weight:600}
.phone-btn svg{flex:none}
.hero-title{font-size:33px;font-weight:600;color:var(--white);line-height:1.22}
.card{position:absolute;top:688px;height:187px;border:1.5px solid var(--orange);border-radius:8px;background:var(--white);box-shadow:0 6px 14px rgba(0,0,0,.06)}
.card .icon{position:absolute;left:26px;top:34px;width:58px;height:58px}
.card h3{position:absolute;left:107px;top:36px;font-size:20px;font-weight:600;line-height:1.2}
.card p{position:absolute;left:107px;font-size:13px;line-height:1.2;color:var(--muted);width:200px}
.eyebrow{font-size:13px;color:var(--orange);letter-spacing:.2px}
.checks{list-style:none}
.checks li{display:flex;align-items:center;gap:11px;font-size:13px;height:26.7px}
.field{position:absolute;border:1px solid var(--line);background:var(--white);border-radius:3px;font-size:12.5px;color:#9aa2ae;padding:10px 24px}
.feature h3{font-size:21px;font-weight:600;line-height:1.2}
.feature p{font-size:13px;line-height:1.22;color:var(--muted);margin-top:10px}
.feature .badge{position:absolute;border-radius:50%;background:var(--navy)}
.footer{position:absolute;left:0;top:3567px;width:1200px;height:243px;background:var(--navy);color:var(--white)}
.footer h4{font-size:13px;font-weight:600;letter-spacing:.3px}
.footer .links{font-size:13px;line-height:24.5px}
</style>
</head>
<body>

<header>
  <div class="brand-box" style="left:93px;top:10px;width:127px;height:70px">BREL<br>Roofing</div>
  <nav class="nav">
    <a class="active">Home</a><a>Services</a><a>Gallery</a><a>About Us</a><a>Contact Us</a>
  </nav>
  <div class="phone-btn" style="left:950px;top:20px;width:155px;height:42px;background:var(--orange);color:var(--white);font-size:13.5px;padding-left:14px">
    <svg width="24" height="24" viewBox="0 0 24 24"><circle cx="12" cy="12" r="11" fill="#fff"/><path d="M7 7c1-1 2 0 2.5 1.5l-1 1c.5 1.5 1.8 2.8 3.3 3.3l1-1c1.5.5 2.5 1.5 1.5 2.5-2 2-8-3.5-7.3-7.3z" fill="var(--orange)"/></svg>
    555-014-2290
  </div>
</header>

<section>
  <div class="abs" style="left:0;top:96px;width:392px;height:552px;background:var(--navy)"></div>
  <div class="photo" role="img" aria-label="New York skyline across the water with a roofer installing a flat roof in the foreground" style="left:392px;top:96px;width:808px;height:552px;background:linear-gradient(180deg,#cfe0ef 0%,#aac4dc 45%,#6f8aa5 62%,#3e5a78 72%,#c9ccd0 78%,#e2e3e5 100%)"></div>
  <svg class="abs" style="left:58px;top:208px" width="474" height="378" viewBox="0 0 474 378"><polygon points="0,0 427,0 474,378 0,378" fill="var(--orange)"/></svg>
  <h1 class="abs hero-title" style="left:93px;top:258px;width:360px">Professional &amp; Affordable Roofing Services.</h1>
  <p class="abs" style="left:93px;top:396px;font-size:26px;color:var(--white)">Call Today For a Free Quote!</p>
  <div class="phone-btn" style="left:93px;top:463px;width:164px;height:39px;background:var(--white);color:var(--ink);font-size:13.5px;padding-left:18px">
    <svg width="24" height="24" viewBox="0 0 24 24"><circle cx="12" cy="12" r="11" fill="var(--navy)"/><path d="M7 7c1-1 2 0 2.5 1.5l-1 1c.5 1.5 1.8 2.8 3.3 3.3l1-1c1.5.5 2.5 1.5 1.5 2.5-2 2-8-3.5-7.3-7.3z" fill="#fff"/></svg>
    555-014-2290
  </div>
</section>

<section>
  <div class="card" style="left:93px;width:327px">
    <svg class="icon" viewBox="0 0 58 58" role="img" aria-label="Roof leak icon"><path d="M29 6c8 12 13 19 13 26a13 13 0 0 1-26 0c0-7 5-14 13-26z" fill="var(--orange)"/><rect x="4" y="48" width="50" height="6" fill="var(--orange)"/></svg>
    <h3>Roof Leaks Repair</h3>
    <p style="top:70px">Lorem ipsum dolor sit amet consectetur. Dui pellentesque quisque venenatis at. Faucibus eu cursus ut integer.</p>
  </div>
  <div class="card" style="left:440px;width:327px">
    <svg class="icon" viewBox="0 0 58 58" role="img" aria-label="Flashing service icon"><polygon points="2,56 56,56 56,30" fill="var(--orange)"/><circle cx="22" cy="18" r="7" fill="var(--orange)"/><circle cx="50" cy="4" r="3.5" fill="none" stroke="var(--orange)" stroke-width="1.5"/></svg>
    <h3>Flashing Services</h3>
    <p style="top:70px">Lorem ipsum dolor sit amet consectetur. Dui pellentesque quisque venenatis at. Faucibus eu cursus ut integer.</p>
  </div>
  <div class="card" style="left:780px;width:328px">
    <svg class="icon" viewBox="0 0 58 58" role="img" aria-label="Waterproofing helmet icon"><path d="M8 30a21 21 0 0 1 42 0z" fill="var(--orange)"/><rect x="4" y="30" width="50" height="6" rx="2" fill="var(--orange)"/><circle cx="29" cy="46" r="9" fill="none" stroke="var(--orange)" stroke-width="4"/></svg>
    <h3 style="left:97px;top:26px">Wateprooping<br>Expert</h3>
    <p style="left:97px;top:79px">Lorem ipsum dolor sit amet consectetur. Dui pellentesque quisque venenatis at. Faucibus eu cursus ut integer.</p>
  </div>
</section>

<section>
  <p class="abs eyebrow" style="left:100px;top:950px">ABOUT BREL Roofing</p>
  <h2 class="abs" style="left:100px;top:980px;width:430px;font-size:27px;font-weight:800;line-height:1.2">EXPERT FLAT ROOF SERVICES: PROS IN ALL ASPECTS OF ROOFING</h2>
  <p class="abs" style="left:97px;top:1092px;width:420px;font-size:13px;line-height:1.2;color:var(--muted)">At BREL Roofing, we are a trusted and reputable roofing company specializing in new construction flat roof installation and repair. With years of experience in the industry, we take pride in providing exceptional roofing solutions to our valued clients.</p>
  <ul class="abs checks" style="left:97px;top:1171px">
    <li><svg width="16" height="16" viewBox="0 0 16 16"><circle cx="8" cy="8" r="8" fill="var(--orange)"/><path d="M4.5 8.3l2.4 2.3 4.6-4.8" stroke="#fff" stroke-width="1.8" fill="none"/></svg>Licensed Bonded &amp; Insured</li>
    <li><svg width="16" height="16" viewBox="0 0 16 16"><circle cx="8" cy="8" r="8" fill="var(--orange)"/><path d="M4.5 8.3l2.4 2.3 4.6-4.8" stroke="#fff" stroke-width="1.8" fill="none"/></svg>Reliable &amp; Experienced Professional</li>
    <li><svg width="16" height="16" viewBox="0 0 16 16"><circle cx="8" cy="8" r="8" fill="var(--orange)"/><path d="M4.5 8.3l2.4 2.3 4.6-4.8" stroke="#fff" stroke-width="1.8" fill="none"/></svg>Free Evaluation &amp; Estimates</li>
    <li><svg width="16" height="16" viewBox="0 0 16 16"><circle cx="8" cy="8" r="8" fill="var(--orange)"/><path d="M4.5 8.3l2.4 2.3 4.6-4.8" stroke="#fff" stroke-width="1.8" fill="none"/></svg>Lead-Safe Certified</li>
    <li><svg width="16" height="16" viewBox="0 0 16 16"><circle cx="8" cy="8" r="8" fill="var(--orange)"/><path d="M4.5 8.3l2.4 2.3 4.6-4.8" stroke="#fff" stroke-width="1.8" fill="none"/></svg>24/7 Emergency Services</li>
    <li><svg width="16" height="16" viewBox="0 0 16 16"><circle cx="8" cy="8" r="8" fill="var(--orange)"/><path d="M4.5 8.3l2.4 2.3 4.6-4.8" stroke="#fff" stroke-width="1.8" fill="none"/></svg>Top-Rated Local Business</li>
  </ul>
  <div class="abs" style="left:97px;top:1350px;width:133px;height:38px;background:var(--navy);color:var(--white);border-radius:4px;font-size:13px;font-weight:600;display:flex;align-items:center;justify-content:center;gap:10px">Read More
    <svg width="14" height="12" viewBox="0 0 14 12"><path d="M1 6h11M7.5 1.5 12 6l-4.5 4.5" stroke="#fff" stroke-width="1.6" fill="none"/></svg>
  </div>
  <div class="photo" role="img" aria-label="Roofer in a yellow hard hat kneeling on a flat roof" style="left:603px;top:973px;width:281px;height:413px;border-radius:12px;background:linear-gradient(180deg,#dfe6e6 0%,#b9c6c4 35%,#6d7b86 60%,#c8cbcf 100%)"></div>
  <div class="photo" role="img" aria-label="Finished dark flat roof on a brick building" style="left:903px;top:992px;width:204px;height:367px;border-radius:12px;background:linear-gradient(160deg,#9bb38a 0%,#6e7470 30%,#555b63 60%,#8a6a58 100%)"></div>
  <div class="abs" style="left:507px;top:1245px;width:205px;height:70px;background:var(--white);border-radius:8px;box-shadow:0 8px 22px rgba(0,0,0,.12);display:flex;align-items:center;gap:12px;padding-left:14px">
    <svg width="42" height="42" viewBox="0 0 42 42"><rect width="42" height="42" rx="8" fill="var(--orange)"/><circle cx="21" cy="21" r="12" fill="#fff"/><path d="M15 15c1-1 2 0 2.5 1.5l-1 1c.5 1.5 1.8 2.8 3.3 3.3l1-1c1.5.5 2.5 1.5 1.5 2.5-2 2-8-3.5-7.3-7.3z" fill="var(--orange)"/></svg>
    <div><div style="font-size:10px;color:var(--muted)">24/7 Emergency Services</div><div style="font-size:16.5px;font-weight:600;color:var(--navy);margin-top:2px">555-014-2290</div></div>
  </div>
</section>

<section class="abs" style="left:0;top:1472px;width:1200px;height:566px;background:var(--navy)">
  <h2 class="abs" style="left:0;top:62px;width:1200px;text-align:center;font-size:26px;font-weight:600;color:var(--white)">PROJECT GALLERY</h2>
  <div class="photo" role="img" aria-label="Roofers working on a tall building roof" style="left:97px;top:117px;width:177px;height:358px;background:linear-gradient(180deg,#b8c9d8 0%,#d8dcdf 30%,#a9acaf 80%,#7a6a58 100%)"></div>
  <div class="photo" role="img" aria-label="Large flat roof with standing seam metal section under blue sky" style="left:298px;top:117px;width:603px;height:358px;background:linear-gradient(180deg,#6f9fd6 0%,#a9c8e8 30%,#8c99a6 42%,#3f5675 60%,#2d3e58 100%)"></div>
  <div class="photo" role="img" aria-label="Metal roof panels under a cloudy sky" style="left:924px;top:117px;width:178px;height:358px;background:linear-gradient(180deg,#5e6a74 0%,#9ea7ad 35%,#6f8c8c 60%,#4e6d70 100%)"></div>
  <svg class="abs" style="left:97px;top:274px" width="42" height="42" viewBox="0 0 42 42"><circle cx="21" cy="21" r="21" fill="#fff"/><path d="M27 21H15M20 16l-5 5 5 5" stroke="var(--ink)" stroke-width="1.8" fill="none"/></svg>
  <svg class="abs" style="left:1060px;top:274px" width="42" height="42" viewBox="0 0 42 42"><rect width="42" height="42" fill="#fff"/><path d="M15 21h12M22 16l5 5-5 5" stroke="var(--ink)" stroke-width="1.8" fill="none"/></svg>
</section>

<section class="abs" style="left:0;top:2038px;width:1200px;height:515px;background:linear-gradient(120deg,#f4f6fa 0%,#e6ebf2 50%,#f2f4f8 100%)">
  <div class="photo" role="img" aria-label="Two roofers torching a membrane onto a flat roof" style="left:105px;top:65px;width:420px;height:373px;border-radius:24px;background:linear-gradient(180deg,#dfe5ea 0%,#b9c4cd 25%,#2d4a84 55%,#7a8088 80%,#9aa0a6 100%)"></div>
  <p class="abs eyebrow" style="left:621px;top:82px">TESTIMONIALS</p>
  <h2 class="abs" style="left:621px;top:112px;width:400px;font-size:27px;font-weight:600;line-height:1.28">Some of Our Happy Clients Says</h2>
  <svg class="abs" style="left:628px;top:200px" width="40" height="32" viewBox="0 0 40 32"><path d="M0 32V16C0 6 5 1 16 0v6c-5 1-8 4-8 9h8v17zM22 32V16c0-10 5-15 16-16v6c-5 1-8 4-8 9h8v17z" fill="var(--orange)"/></svg>
  <p class="abs" style="left:624px;top:253px;width:445px;font-size:13px;line-height:1.2;color:var(--muted)">Lorem ipsum dolor sit amet consectetur. Felis odio ac vitae augue mi eget odio convallis feugiat. Fames vestibulum odio amet quis faucibus. Ornare mauris eget odio lorem dui viverra diam adipiscing volutpat. Egestas duis viverra sem libero scelerisque sodales. Ac ullamcorper.</p>
  <div class="abs" role="img" aria-label="Client portrait" style="left:630px;top:340px;width:44px;height:44px;border-radius:50%;background:#cfcfcf;border:2px solid #f3c9a8"></div>
  <p class="abs" style="left:684px;top:346px;font-size:13px;font-weight:600">Marta Velin</p>
  <p class="abs" style="left:684px;top:364px;font-size:11px;color:var(--muted)">New York City</p>
  <div class="abs" style="left:1000px;top:386px;width:100px;height:3px;background:#f6d4bd"></div>
  <div class="abs" style="left:1000px;top:386px;width:33px;height:3px;background:var(--orange)"></div>
</section>

<section>
  <div class="abs" style="left:0;top:2553px;width:1200px;height:522px;background:var(--orange)"></div>
  <p class="abs" style="left:93px;top:2634px;font-size:13px;color:var(--white)">Your roof require professional attention</p>
  <h2 class="abs" style="left:93px;top:2660px;font-size:27px;font-weight:600;color:var(--white)">Book Your Appointment</h2>
  <div class="abs" style="left:93px;top:2718px;width:1015px;height:490px;border-radius:20px;background:linear-gradient(135deg,#eef1f6 0%,#ffffff 45%,#e7ebf2 100%)"></div>
  <div class="field" style="left:163px;top:2794px;width:258px;height:40px">First name</div>
  <div class="field" style="left:438px;top:2794px;width:258px;height:40px">Last name</div>
  <div class="field" style="left:163px;top:2849px;width:258px;height:40px">Phone number</div>
  <div class="field" style="left:438px;top:2849px;width:258px;height:40px">Email</div>
  <div class="field" style="left:163px;top:2904px;width:533px;height:58px">Address</div>
  <div class="field" style="left:163px;top:2976px;width:258px;height:39px">City/Town
    <svg class="abs" style="right:14px;top:15px" width="12" height="8" viewBox="0 0 12 8"><path d="M1 1l5 5 5-5" stroke="var(--ink)" stroke-width="1.6" fill="none"/></svg></div>
  <div class="field" style="left:438px;top:2976px;width:258px;height:39px">State
    <svg class="abs" style="right:14px;top:15px" width="12" height="8" viewBox="0 0 12 8"><path d="M1 1l5 5 5-5" stroke="var(--ink)" stroke-width="1.6" fill="none"/></svg></div>
  <div class="field" style="left:163px;top:3031px;width:533px;height:86px;padding-left:20px">Message</div>
  <div class="abs" style="left:163px;top:3134px;width:533px;height:38px;background:var(--orange);border-radius:4px;color:var(--white);font-size:13px;font-weight:500;display:flex;align-items:center;justify-content:center;gap:10px">REQUEST SUBMIT NOW
    <svg width="14" height="12" viewBox="0 0 14 12"><path d="M1 6h11M7.5 1.5 12 6l-4.5 4.5" stroke="#fff" stroke-width="1.6" fill="none"/></svg></div>
  <div class="photo" role="img" aria-label="Roofing worker in orange hard hat and high-visibility vest with arms crossed" style="left:755px;top:2655px;width:315px;height:553px;border-radius:40% 40% 0 0 / 18% 18% 0 0;background:linear-gradient(180deg,#f58a2a 0%,#f58a2a 12%,#c99c7d 22%,#2b2b2b 40%,#d8ef2a 55%,#c6dd24 85%,#e7ebf2 100%)"></div>
</section>

<section>
  <div class="feature">
    <div class="badge" style="left:88px;top:3307px;width:72px;height:72px"><svg width="72" height="72" viewBox="0 0 72 72"><circle cx="36" cy="34" r="14" fill="var(--orange)"/><path d="M28 44l-4 12 8-4 4 6M44 44l4 12-8-4-4 6" fill="var(--orange)"/></svg></div>
    <div class="abs" style="left:173px;top:3316px;width:225px">
      <h3>Reliable Roofing Professionals</h3>
      <p>As specialists in residential and commercial roofing  services, we are dedicated to providing customer service that is second to none. Whether you have a new construction project or it is time for repairs, we offer the roofing services you need.</p>
    </div>
  </div>
  <div class="feature">
    <div class="badge" style="left:445px;top:3307px;width:72px;height:72px"><svg width="72" height="72" viewBox="0 0 72 72"><path d="M16 42 36 26l20 16v4H16z" fill="var(--orange)"/></svg></div>
    <div class="abs" style="left:525px;top:3316px;width:230px">
      <h3>Individualized Roofing Options</h3>
      <p>We provide a full consultation to explain your available options so that you can choose the roofing plan that's right for your home or business. We will work with you and adhere to your personal needs, and then we'll be in contact through the whole project.</p>
    </div>
  </div>
  <div class="feature">
    <div class="badge" style="left:787px;top:3314px;width:72px;height:72px"><svg width="72" height="72" viewBox="0 0 72 72"><path d="M36 22l12 4v10c0 8-5 12-12 15-7-3-12-7-12-15V26z" fill="none" stroke="var(--orange)" stroke-width="2.5"/><path d="M31 36l4 4 7-7" stroke="var(--orange)" stroke-width="2.5" fill="none"/></svg></div>
    <div class="abs" style="left:872px;top:3323px;width:270px">
      <h3 style="white-space:nowrap">Satisfaction Guaranteed</h3>
      <p style="margin-left:5px;width:235px">We strive to save you both time and money by combining roofing knowledge, the highest quality parts and equipment, and dedication to delivering exceptional service. We will not leave the job until it is finished and you are satisfied with the results.</p>
    </div>
  </div>
</section>

<footer class="footer">
  <div class="brand-box" style="left:93px;top:48px;width:127px;height:70px;border-color:#fff;color:#fff">BREL<br>Roofing</div>
  <div class="abs" style="left:95px;top:143px;display:flex;gap:12px">
    <span style="width:15px;height:15px;border-radius:50%;background:var(--orange)"></span>
    <span style="width:15px;height:15px;border-radius:50%;background:var(--orange)"></span>
    <span style="width:15px;height:15px;border-radius:50%;background:var(--orange)"></span>
    <span style="width:15px;height:15px;border-radius:50%;background:var(--orange)"></span>
    <span style="width:15px;height:15px;border-radius:50%;background:var(--orange)"></span>
  </div>
  <h4 class="abs" style="left:372px;top:50px">CONTACT US</h4>
  <div class="abs links" style="left:373px;top:76px">
    <div style="display:flex;gap:12px;align-items:center"><svg width="15" height="12" viewBox="0 0 15 12"><rect x=".75" y=".75" width="13.5" height="10.5" fill="none" stroke="var(--orange)" stroke-width="1.4"/><path d="M1 1l6.5 5L14 1" stroke="var(--orange)" stroke-width="1.4" fill="none"/></svg>hello@brelroofing.example</div>
    <div style="display:flex;gap:12px;align-items:center"><svg width="15" height="15" viewBox="0 0 24 24"><path d="M5 3c2-2 4 0 5 3l-2 2c1 3 4 6 7 7l2-2c3 1 5 3 3 5-4 4-17-9-15-15z" fill="none" stroke="var(--orange)" stroke-width="2"/></svg>555-014-2290</div>
    <div style="display:flex;gap:12px;align-items:flex-start;margin-top:6px;line-height:17px"><svg width="15" height="15" viewBox="0 0 16 16" style="margin-top:2px"><circle cx="8" cy="8" r="7" fill="none" stroke="var(--orange)" stroke-width="1.4"/><path d="M8 4v4l3 2" stroke="var(--orange)" stroke-width="1.4" fill="none"/></svg><span>Monday - Friday: 8am - 5pm<br>Saturday - Sunday: 8am-12</span></div>
  </div>
  <h4 class="abs" style="left:705px;top:46px">QUICKLINKS</h4>
  <div class="abs links" style="left:708px;top:68px">
    <div style="color:var(--orange)">Home</div><div>Services</div><div>Gallery</div><div>About Us</div><div>Contact Us</div>
  </div>
  <p class="abs" style="left:892px;top:43px;width:210px;font-size:13px;line-height:1.2">Sign up to receive maintenance reminders and hear about our latest projects.</p>
  <div class="abs" style="left:892px;top:100px;width:205px;height:31px;background:#fff;border-radius:3px;color:var(--ink);font-size:13px;padding:8px 14px">Email</div>
  <div class="abs" style="left:892px;top:140px;width:205px;height:33px;background:var(--orange);border-radius:3px;font-size:13px;font-weight:500;display:flex;align-items:center;justify-content:center">SIGN UP</div>
  <div class="abs" style="left:0;top:205px;width:1200px;height:1px;background:rgba(255,255,255,.15)"></div>
  <p class="abs" style="left:0;top:218px;width:1200px;text-align:center;font-size:10px">COPYRIGHT © 2023 BREL ROOFING - ALL RIGHTS RESERVED.</p>
</footer>

</body>
</html>
```